Veteran Owned General Contractor needs Bold New Business Cards

We are a service disabled veteran owned small business. We're a general contractor that specializes in excavation, underground utilities, site work, land clearing and demolition. We would like a fresh, simple, bold, new look for our business cards. We're open to ideas! We'd like to incorporate the following information on the card:

Company Name & Logo, Name of Person, Job Title, Office Phone, Fax, Cell Phone, Email Address, Website, SDVOSB

Our logo is included. We look forward to your thoughts.

Thank you!
Updates

Reason: Hello Due to the overwhelming response to this project, we are extending the deadline one time to allow for improved communication and feedback with the top candidates. We would like to thank everyone for their hard work and exceptional creativity! Thank you

Industry/Entity Type

Business

Contact Information for Business Card

Font styles to use
Sans Serif

Requirements
Nice to have
• As we are a veteran owned company, it would be nice to incorporate an American flag into the design. Maybe on the back?

```html
<!DOCTYPE html>
<html lang="en">
<head>
<meta charset="utf-8">
<title>Stonebrook Inc — Business Cards</title>
<link rel="stylesheet" href="https://fonts.googleapis.com/css2?family=Saira:wght@400;500;600;800&display=swap">
<style>
  :root {
    --green: #6dbd45;
    --green-dark: #5aa436;
    --ink: #1a1a1a;
    --charcoal: #2a2a2a;
    --grey: #8a8a8a;
    --paper: #ffffff;
    --backdrop: #ececec;
  }
  * { margin: 0; padding: 0; box-sizing: border-box; }
  html, body { width: 1200px; height: 586px; overflow: hidden; }
  body {
    background: var(--backdrop);
    font-family: "Saira", "Arial", sans-serif;
    position: relative;
  }
  .card {
    position: absolute;
    top: 143px;
    width: 502px;
    height: 300px;
    overflow: hidden;
  }
  /* Front */
  .card-front { left: 61px; background: var(--green); }
  .veteran-badge {
    position: absolute;
    left: 399px; top: 19px;
    width: 103px; height: 51px;
    background: var(--paper);
    border-radius: 8px 0 0 8px;
  }
  .front-mark {
    position: absolute;
    left: 215px; top: 87px;
    width: 74px; height: 74px;
    background: var(--charcoal);
    border: 3px solid #6f6f6f;
    border-radius: 12px;
  }
  .front-name {
    position: absolute;
    left: 0; right: 0; top: 180px;
    text-align: center;
    color: var(--paper);
    font-weight: 800;
    font-size: 40px;
    letter-spacing: 1px;
    line-height: 1;
  }
  .front-web {
    position: absolute;
    left: 0; right: 0; top: 258px;
    text-align: center;
    color: var(--ink);
    font-weight: 600;
    font-size: 12.5px;
    letter-spacing: 2.4px;
  }
  /* Back */
  .card-back { left: 619px; background: var(--paper); }
  .back-brand {
    position: absolute;
    left: 103px; top: 47px;
    display: flex; align-items: center; gap: 10px;
  }
  .back-mark {
    width: 42px; height: 42px;
    background: var(--charcoal);
    border: 2px solid #6f6f6f;
    border-radius: 8px;
  }
  .back-name {
    color: var(--green);
    font-weight: 800;
    font-size: 33px;
    letter-spacing: 0.5px;
    line-height: 1;
  }
  .person {
    position: absolute;
    right: calc(502px - 216px); top: 158px;
    text-align: right;
  }
  .person-name { color: var(--green); font-weight: 600; font-size: 18px; line-height: 1.2; }
  .person-title { color: #333; font-size: 10.5px; line-height: 1.3; }
  .address {
    position: absolute;
    right: calc(502px - 216px); top: 213px;
    text-align: right;
    color: var(--ink);
    font-weight: 600;
    font-size: 12.5px;
    line-height: 1.35;
  }
  .divider {
    position: absolute;
    left: 244px; top: 155px;
    width: 2px; height: 104px;
    background: linear-gradient(to bottom, transparent, var(--green) 40%, var(--green) 60%, transparent);
  }
  .contacts {
    position: absolute;
    left: 274px; top: 158px;
    list-style: none;
  }
  .contacts li {
    display: flex; align-items: center; gap: 8px;
    height: 24px;
    font-size: 12px;
    color: var(--ink);
  }
  .contact-icon {
    width: 17px; height: 17px;
    border-radius: 50%;
    background: var(--green);
    display: flex; align-items: center; justify-content: center;
  }
  .band-green { position: absolute; left: 0; right: 0; top: 284px; height: 9px; background: var(--green); }
  .band-grey { position: absolute; left: 0; right: 0; top: 293px; height: 7px; background: var(--grey); }
</style>
</head>
<body>
  <section class="card card-front" aria-label="Card front">
    <div class="veteran-badge" aria-hidden="true"></div>
    <div class="front-mark" aria-hidden="true"></div>
    <div class="front-name">STONEBROOK INC</div>
    <div class="front-web">www.stonebrookco.com</div>
  </section>

  <section class="card card-back" aria-label="Card back">
    <div class="back-brand">
      <div class="back-mark" aria-hidden="true"></div>
      <div class="back-name">STONEBROOK INC</div>
    </div>

    <div class="person">
      <div class="person-name">Dana Whitfield</div>
      <div class="person-title">Owner / Founder</div>
    </div>
    <div class="address">820 Alder Ridge Road<br>Fairview, OR 97024</div>

    <div class="divider"></div>

    <ul class="contacts">
      <li>
        <span class="contact-icon"><svg width="9" height="11" viewBox="0 0 9 11"><rect x="1" y="0.5" width="7" height="10" rx="1.2" fill="none" stroke="#fff" stroke-width="1.2"/><circle cx="4.5" cy="8.5" r="0.7" fill="#fff"/></svg></span>
        (555) 014 220
      </li>
      <li>
        <span class="contact-icon"><svg width="11" height="9" viewBox="0 0 11 9"><path d="M1 3 Q5.5 -0.5 10 3 L8.5 4 L7.5 2.8 L3.5 2.8 L2.5 4 Z" fill="#fff"/><rect x="2.5" y="4.5" width="6" height="4" rx="0.8" fill="#fff"/></svg></span>
        555-201-4470
      </li>
      <li>
        <span class="contact-icon"><svg width="11" height="10" viewBox="0 0 11 10"><rect x="3" y="0.5" width="5" height="3" fill="#fff"/><rect x="0.5" y="3.5" width="10" height="4" rx="1" fill="#fff"/><rect x="3" y="6.5" width="5" height="3" fill="#fff" stroke="#6dbd45" stroke-width="0.6"/></svg></span>
        1-800-555-0199
      </li>
      <li>
        <span class="contact-icon"><svg width="10" height="8" viewBox="0 0 10 8"><rect x="0.5" y="0.5" width="9" height="7" fill="none" stroke="#fff" stroke-width="1"/><path d="M0.5 0.5 L5 4.5 L9.5 0.5" fill="none" stroke="#fff" stroke-width="1"/></svg></span>
        dana@stonebrookco.com
      </li>
    </ul>

    <div class="band-green"></div>
    <div class="band-grey"></div>
  </section>
</body>
</html>
```